New Website Design for Rides for Heroes.org - A Site for People to Donate Cars to War / Disabled Ve

Current site: www.ridesforheroes.org; Look at these sites for ideas: bykes2tots.org; motorsfordreams.org; www.autosforourcadets.org; www.trucksforheroes.org

Industry/Entity Type

Charity

Coding

Coded - Design and coding required

Number of Pages Required

1 page

Requirements
Must have
• n/a
Nice to have
• n/a
Should not have
• n/a

```html
<!DOCTYPE html>
<html lang="en">
<head>
<meta charset="utf-8">
<title>Rides for Heroes – Donate your car</title>
<link rel="stylesheet" href="https://fonts.googleapis.com/css2?family=Roboto:wght@400;500;700&family=Signika:wght@300;400;600&display=swap">
<style>
:root{
  --blue:#2f9ce0;
  --blue-title:#1b7cc2;
  --navy:#1a5a96;
  --green:#7cc243;
  --green-text:#8cc63f;
  --grey-bg:#efefef;
  --badge:#d3d8de;
  --text:#555;
  --text-dark:#333;
  --maroon:#760019;
  --red:#b3161d;
  --white:#fff;
}
*{margin:0;padding:0;box-sizing:border-box}
html,body{width:677px;height:1200px;overflow:hidden}
body{font-family:"Roboto",Arial,sans-serif;color:var(--text);background:var(--white);position:relative}
.abs{position:absolute}

/* header */
.site-header{left:0;top:0;width:677px;height:50px;background:linear-gradient(#2a6fb9,#1e63ad);border-bottom:3px solid var(--red)}
.brand{left:52px;top:15px;display:flex;align-items:center;gap:5px;color:var(--white);font-size:13px;font-weight:500}
.brand-mark{width:14px;height:14px;border-radius:50%;background:var(--red)}
.main-nav{left:248px;top:21px;font-size:7.5px;color:var(--white);text-transform:uppercase}
.main-nav span{position:absolute;white-space:nowrap}
.help{right:92px;top:8px;text-align:right;color:var(--white);line-height:1.1}
.help .small{font-size:9.5px}
.help .call{font-size:11px;font-weight:700}
.help .live{font-size:6.5px}
.chat-icon{left:588px;top:10px}

/* hero */
.hero{left:0;top:50px;width:677px;height:286px;background:var(--blue)}
.hero-title{left:51px;top:102px;font-family:"Signika",sans-serif;font-weight:300;font-size:28px;line-height:30px;color:var(--white);letter-spacing:-.6px}
.hero-title strong{font-weight:600;display:block}
.hero-photo{left:0;top:184px;width:320px;height:152px;border-radius:0 60px 0 0;background:linear-gradient(180deg,#2f9a48 0%,#2a8a40 35%,#e8ebe9 55%,#c9cfcc 100%)}
.donate-card{left:363px;top:80px;width:259px;height:230px;background:var(--white);box-shadow:0 0 4px rgba(0,0,0,.25)}
.donate-card .kicker{position:absolute;left:0;width:100%;top:12px;text-align:center;font-size:13px;color:var(--blue-title)}
.donate-card h2{position:absolute;left:0;width:100%;top:24px;text-align:center;font-size:19px;font-weight:700;color:var(--blue-title)}
.donate-card .note{position:absolute;left:0;width:100%;top:48px;text-align:center;font-size:8.6px;color:var(--text-dark)}
.field{position:absolute;width:117px;height:21px;border:1px solid #ccc;font-size:6.5px;color:#888;padding:7px 0 0 5px}
.btn-donate{position:absolute;left:10px;top:190px;width:239px;height:24px;background:var(--green);color:var(--white);font-size:9px;font-weight:700;text-align:center;line-height:24px}

/* how */
.section-title{left:0;width:677px;text-align:center;font-family:"Signika",sans-serif;font-weight:300;font-size:21px;color:var(--blue-title)}
.step{width:120px;text-align:center}
.step-circle{width:54px;height:54px;border:1.5px solid var(--green);border-radius:50%;margin:0 auto;display:flex;align-items:center;justify-content:center}
.step-label{margin-top:10px;font-size:9.5px;font-weight:700;color:var(--text-dark)}
.wave{top:452px}

/* why */
.why{left:0;top:560px;width:677px;height:264px;background:var(--grey-bg)}
.benefit{width:184px;font-size:7.3px;line-height:12px;padding-left:15px;color:var(--text)}
.benefit b{color:#444;font-weight:700}
.benefit svg{position:absolute;left:0;top:2px}
.tow-photo{left:250px;top:656px;width:178px;height:118px;border-radius:8px;background:linear-gradient(90deg,#f39a2a 0%,#e9862a 45%,#2f78c4 65%,#1f5fa6 100%);opacity:.85}

/* trust */
.trust-badge{top:910px;height:32px;background:var(--badge);border-radius:4px}

/* footer */
.site-footer{left:0;top:996px;width:677px;height:204px;background:var(--maroon);color:var(--white);font-size:7.5px}
.footer-col{top:48px}
.footer-col h3{font-size:9.5px;font-weight:400;color:var(--green-text);margin-bottom:9px}
.footer-col p,.footer-col li{line-height:14px;list-style:none}
.email-field{width:132px;height:22px;background:var(--white);color:#777;font-size:6.5px;padding:8px 0 0 5px}
.btn-send{margin-top:6px;width:53px;height:21px;background:var(--navy);color:var(--white);font-size:6.5px;display:flex;align-items:center;justify-content:center;gap:3px}
.follow{margin-top:8px;color:var(--green-text);font-size:9px;display:flex;align-items:center;gap:6px}
.follow i{width:7px;height:7px;border-radius:50%;background:var(--white);display:inline-block}
.copyright{left:0;width:677px;top:183px;text-align:center;font-size:7px}
</style>
</head>
<body>

<header class="site-header abs">
  <div class="brand abs"><span class="brand-mark"></span>Rides for Heroes</div>
  <nav class="main-nav abs">
    <span style="left:0">Home</span>
    <span style="left:38px">How it works</span>
    <span style="left:105px">Why us</span>
    <span style="left:148px">Contact</span>
  </nav>
  <div class="help abs">
    <div class="small">we need your help</div>
    <div class="call">Call 1-800-555-0142</div>
    <div class="live">Live operators Available(24X7)</div>
  </div>
  <svg class="chat-icon abs" width="36" height="30" viewBox="0 0 36 30" fill="none" stroke="#7fc0ef" stroke-width="1.6">
    <ellipse cx="13" cy="11" rx="11" ry="8"/>
    <path d="M7 17 L5 23 L12 18"/>
    <ellipse cx="23" cy="17" rx="10" ry="7"/>
    <path d="M28 22 L30 27 L25 23"/>
  </svg>
</header>

<section class="hero abs"></section>
<h1 class="hero-title abs">Donate your car to a wet,<strong>make a difference</strong></h1>
<div class="hero-photo abs" role="img" aria-label="Green and white classic pickup truck, front view"></div>

<form class="donate-card abs">
  <div class="kicker">DONATE</div>
  <h2>YOUR CAR HERE!</h2>
  <div class="note">Please fill out form or Call toll-free 1-800-555-0142</div>
  <div class="field" style="left:10px;top:71px">Name</div>
  <div class="field" style="left:131px;top:71px">Email</div>
  <div class="field" style="left:10px;top:100px">Phone Number</div>
  <div class="field" style="left:131px;top:100px">Cell Phone</div>
  <div class="field" style="left:10px;top:130px">Address</div>
  <div class="field" style="left:131px;top:130px">City</div>
  <div class="field" style="left:10px;top:158px">State</div>
  <div class="field" style="left:131px;top:158px">Zip Code</div>
  <div class="btn-donate">DONATE NOW</div>
</form>

<h2 class="section-title abs" style="top:374px">How it works</h2>

<div class="step abs" style="left:82px;top:431px">
  <div class="step-circle">
    <svg width="30" height="30" viewBox="0 0 24 24" fill="none" stroke="#222" stroke-width="1.5" stroke-linejoin="round"><path d="M6 3l3 4-2 2c1 3 4 6 7 7l2-2 4 3-2 3C10 20 4 14 3 5z"/></svg>
  </div>
  <div class="step-label">CALL US</div>
</div>
<svg class="wave abs" style="left:210px" width="58" height="12" viewBox="0 0 58 12"><path d="M1 6 C8 0 14 12 22 6 S36 0 44 6 S54 10 57 5" fill="none" stroke="#aaa" stroke-width="1.2"/></svg>
<div class="step abs" style="left:277px;top:431px">
  <div class="step-circle">
    <svg width="32" height="26" viewBox="0 0 32 26" fill="none" stroke="#222" stroke-width="1.5"><path d="M2 18h26v-6l-4-5h-6v11"/><path d="M2 18V12l10-4"/><circle cx="8" cy="21" r="3"/><circle cx="23" cy="21" r="3"/></svg>
  </div>
  <div class="step-label">WE TOW IT</div>
</div>
<svg class="wave abs" style="left:406px" width="58" height="12" viewBox="0 0 58 12"><path d="M1 6 C8 0 14 12 22 6 S36 0 44 6 S54 10 57 5" fill="none" stroke="#aaa" stroke-width="1.2"/></svg>
<div class="step abs" style="left:473px;top:431px">
  <div class="step-circle">
    <svg width="28" height="28" viewBox="0 0 24 24" fill="none" stroke="#222" stroke-width="1.5" stroke-linejoin="round"><path d="M16 3l5 5L9 20H4v-5z"/><path d="M13 6l5 5"/></svg>
  </div>
  <div class="step-label">TAX WRITE-OFF</div>
</div>

<section class="why abs"></section>
<h2 class="section-title abs" style="top:596px">Why donate your car to us?</h2>

<div class="benefit abs" style="left:52px;top:654px"><svg width="11" height="9" viewBox="0 0 11 9"><path d="M1 5l3 3 6-7" fill="none" stroke="#7cc243" stroke-width="1.5"/></svg><b>TrustMark A+ Rated &amp; IRS 501(c)3 Approved:</b> Free 24/7 Pickup with No DMV Hassles.</div>
<div class="benefit abs" style="left:52px;top:692px"><svg width="11" height="9" viewBox="0 0 11 9"><path d="M1 5l3 3 6-7" fill="none" stroke="#7cc243" stroke-width="1.5"/></svg><b>Free Local Towing:</b> We will pick up your car donation, running or not, when it's most convenient, at home or work.</div>
<div class="benefit abs" style="left:52px;top:741px"><svg width="11" height="9" viewBox="0 0 11 9"><path d="M1 5l3 3 6-7" fill="none" stroke="#7cc243" stroke-width="1.5"/></svg><b>Car donations help fund programs:</b> And benefit National Heroes Support Fund. An IRS 501(c)3 nonprofit organization.</div>

<div class="tow-photo abs" role="img" aria-label="Blue tow truck carrying an orange car"></div>

<div class="benefit abs" style="left:444px;top:654px"><svg width="11" height="9" viewBox="0 0 11 9"><path d="M1 5l3 3 6-7" fill="none" stroke="#7cc243" stroke-width="1.5"/></svg><b>Income Tax Deduction:</b> We issue you an IRS tax receipt &amp; offer the largest resale network to get you the highest tax write-off possible.</div>
<div class="benefit abs" style="left:444px;top:705px"><svg width="11" height="9" viewBox="0 0 11 9"><path d="M1 5l3 3 6-7" fill="none" stroke="#7cc243" stroke-width="1.5"/></svg><b>No Paperwork Hassles:</b> We take any car and handle everything: DMV, Smog and IRS paperwork.</div>
<div class="benefit abs" style="left:444px;top:754px"><svg width="11" height="9" viewBox="0 0 11 9"><path d="M1 5l3 3 6-7" fill="none" stroke="#7cc243" stroke-width="1.5"/></svg><b>All Cars Accepted:</b> We take your car regardless of its condition or</div>

<h2 class="section-title abs" style="top:858px">Safe &amp; Secure</h2>
<div class="trust-badge abs" style="left:140px;width:114px" role="img" aria-label="Accreditation badge"></div>
<div class="trust-badge abs" style="left:303px;width:56px" role="img" aria-label="Approved charity badge"></div>
<div class="trust-badge abs" style="left:419px;width:92px" role="img" aria-label="Secure site badge"></div>

<footer class="site-footer abs">
  <div class="footer-col abs" style="left:52px;width:180px">
    <h3>About us</h3>
    <p>There are many variations of passages of Lorem Ipsum available, on the majority have suffered alteration in some form, by a injected humour, or randomised words which do look even slightly believable. If you are going to use a passage of the Lorem Ipsum generators.</p>
  </div>
  <div class="footer-col abs" style="left:278px">
    <h3>Useful links</h3>
    <ul><li>Home</li><li>Donate now</li><li>How it works</li><li>Why us?</li></ul>
  </div>
  <div class="footer-col abs" style="left:377px">
    <h3>Support</h3>
    <ul><li>Contact us</li><li>Call us</li><li>Privacy</li><li>terms &amp; services</li></ul>
  </div>
  <div class="footer-col abs" style="left:492px">
    <h3>Subscribe our Newleter for free</h3>
    <div class="email-field">Enter your email address</div>
    <div class="btn-send"><svg width="8" height="7" viewBox="0 0 8 7"><path d="M0 3L8 0 6 7 4 4z" fill="#fff"/></svg>SEND</div>
    <div class="follow">Follow us: <i></i><i></i><i></i><i></i></div>
  </div>
  <div class="copyright abs">©2016 Rides for Heroes. All rights reserved</div>
</footer>

</body>
</html>
```